Create Homepage Header & Search Box for Education Website

This project is relatively small and pays well.
Site: brightvalelearning.org
Project Title:
Redesign slider to be a static image/graphic and include a 3 drop down search box.
Project Summary:
We need a new homepage header for brightvalelearning.org. The logo, top navigation, and social buttons should remain unchanged. The new header needs to include a static graphic or image and a 3 drop down search box. It can also include some text that speaks to the what our site provides. For text suggestions - see below. Placement for the search box should be to the left under the logo. We will remove the slider functionality and need the design to be static.
Below the current slider images are bar graphs and a pie graph. These can remain as is - or you can make design changes. If you make design changes - please be sure the message doesn't change. Also you can submit one version of the design with this removed if you feel like it helps best accomplish our goal of conversion.
Project Objectives:
The primary objective of the deign is to maximize conversion of clicks to the search box. We need users to gravitate to the search box. Additionally the design should convey trust and academic feel.
Target Market:
High School Graduates and people in their 20s looking for college options.
Potential text:
Tagline Option: "Your #1 Resource for an Affordable Online College Education"
Tagline Option: "Find Affordable Online College Options"
Other Details: Brightvale Learning Hub will help you find a more affordable college experience. Look no further to find financial aid information, cost saving tips, and comprehensive college rankings focused on affordability and value.
Or you can also use some placeholder text and I can create the right messaging.
The Search Box:
The search box is pretty standard - you can see examples in the examples below - or in the files I attached. 3 drop downs and a "Search" button.
Examples of some previous designs attached to the project:
These designs are close - but not perfect. These will give you a good general idea for what we need.
Examples of designs at similar websites:
kwpn.org
studyharborhub.net
topmeadowcourses.com

```html
<!DOCTYPE html>
<html lang="en">
<head>
<meta charset="utf-8">
<title>Brightvale Learning Hub – Affordable Online College Education</title>
<link rel="stylesheet" href="https://fonts.googleapis.com/css2?family=Open+Sans:wght@300;400;600&family=Arimo:wght@400;700&family=Oswald:wght@400;500&family=Roboto:wght@500;700;900&display=swap">
<style>
:root{
  --orange:#f26c38;
  --ink:#2b2b2b;
  --muted:#747474;
  --band:#18242b;
  --teal:#0f5a58;
  --stat-orange:#f27a2e;
  --yellow:#fbe43a;
  --amber:#f7a12a;
  --crimson:#9e0d26;
  --white:#ffffff;
  --line:#e2e2e2;
}
*{margin:0;padding:0;box-sizing:border-box}
html,body{width:1200px;height:1158px;overflow:hidden;background:var(--white)}
body{font-family:"Open Sans",Arial,sans-serif;color:var(--ink)}
.page{position:relative;width:1200px;height:1158px;overflow:hidden}
.abs{position:absolute}

/* header */
.site-header{position:absolute;left:0;top:0;width:1200px;height:77px;background:var(--white)}
.brand{position:absolute;left:100px;top:18px;display:flex;align-items:center;gap:8px}
.brand-dot{width:38px;height:38px;border-radius:50%;background:var(--orange)}
.brand-name{font-family:"Open Sans",sans-serif;font-weight:600;font-size:13px;line-height:15px;color:var(--orange)}
.main-nav a{position:absolute;top:28px;font-size:18.5px;color:#333;text-decoration:none;font-weight:400}
.main-nav a.active{color:var(--orange);border-bottom:2px solid var(--orange);padding-bottom:1px}
.social a{position:absolute;top:29px;width:25px;height:25px;border-radius:4px}

/* hero */
.hero{position:absolute;left:0;top:77px;width:1200px;height:339px}
.hero-photo{position:absolute;inset:0;background:linear-gradient(90deg,#cfcfcf 0%,#a9a9a9 30%,#6d5a4e 55%,#3a2c25 72%,#bdbdbd 100%)}
.hero-caption{position:absolute;left:0;top:227px;width:725px;height:112px;background:rgba(40,40,40,.72);color:var(--white)}
.hero-caption h1{position:absolute;left:57px;top:8px;font-family:"Arimo",sans-serif;font-weight:700;font-size:25px;white-space:nowrap}
.hero-caption p{position:absolute;left:64px;top:42px;width:650px;font-family:"Arimo",sans-serif;font-size:14.4px;line-height:19px;color:#eee}

.search-panel{position:absolute;left:784px;top:0;width:374px;height:339px;background:linear-gradient(90deg,var(--yellow) 0%,#fbd23a 50%,var(--amber) 100%)}
.search-head{position:absolute;left:0;top:0;width:374px;height:76px}
.get-info{position:absolute;left:60px;top:16px;font-family:"Oswald",sans-serif;font-size:14px;line-height:20px;color:#222}
.head-rule{position:absolute;left:106px;top:18px;width:2px;height:40px;background:#222}
.search-title{position:absolute;left:120px;top:9px;font-family:"Roboto",sans-serif;font-weight:900;font-size:27px;color:#1d1d1d;letter-spacing:.3px}
.search-sub{position:absolute;left:120px;top:41px;font-family:"Roboto",sans-serif;font-weight:700;font-size:11.5px;color:#1d1d1d}
.step-no{position:absolute;left:38px;font-family:"Arimo",sans-serif;font-size:28px;color:#333}
.select{position:absolute;left:68px;width:275px;height:55px;border-radius:4px;background:rgba(255,255,255,.55);box-shadow:0 2px 4px rgba(0,0,0,.12)}
.select.is-first{background:var(--white);box-shadow:0 3px 6px rgba(0,0,0,.25)}
.select span{position:absolute;left:22px;top:17px;font-family:"Arimo",sans-serif;font-weight:700;font-size:14.5px;color:#333}
.select i{position:absolute;right:38px;top:17px;width:1px;height:22px;background:#aaa}
.select svg{position:absolute;right:13px;top:19px}
.search-btn{position:absolute;left:69px;top:276px;width:276px;height:50px;border-radius:6px;background:linear-gradient(#b3132f,var(--crimson));box-shadow:0 2px 4px rgba(0,0,0,.3);color:var(--white);font-family:"Roboto",sans-serif;font-weight:700;font-size:28px;letter-spacing:3px;text-align:center;line-height:50px}

/* stats band */
.stats{position:absolute;left:0;top:416px;width:1200px;height:116px;background:var(--band);box-shadow:0 3px 4px rgba(0,0,0,.2)}
.stat-bar{position:absolute;left:104px;width:172px;height:38px;border:1px solid #2d3a42}
.stat-bar b{position:absolute;left:0;top:0;height:36px;background:var(--teal)}
.stat-bar span{position:absolute;left:15px;top:1px;font-family:"Oswald",sans-serif;font-size:26px;color:var(--white);white-space:nowrap}
.stat-label{position:absolute;left:295px;font-family:"Oswald",sans-serif;font-weight:500;font-size:21px;color:var(--stat-orange);letter-spacing:-.3px;transform:scaleX(.92);transform-origin:left}
.pie{position:absolute;left:598px;top:11px}
.stats-copy{position:absolute;left:692px;top:14px;width:400px;text-align:center;color:var(--white)}
.stats-copy h2{font-family:"Open Sans",sans-serif;font-weight:400;font-size:17.5px;color:var(--stat-orange);margin-bottom:6px}
.stats-copy p{font-size:12.5px;line-height:18px;letter-spacing:-.2px}

/* feature cards */
.feature{position:absolute;width:306px}
.feature-icon{position:absolute;left:0;top:0;width:80px;height:80px;border-radius:50%;background:var(--orange);display:flex;align-items:center;justify-content:center}
.feature-body{position:absolute;left:95px;top:2px;width:218px}
.feature-body h3{font-weight:300;font-size:17px;line-height:22px;color:#333;margin-bottom:12px}
.feature-body p{font-family:"Arimo",Arial,sans-serif;font-size:12.6px;line-height:21.5px;color:var(--muted)}
.read-more{position:absolute;right:0;width:76px;height:23px;border:1px solid var(--line);font-family:"Arimo",Arial,sans-serif;font-size:11.5px;color:#b4301c;text-align:center;line-height:21px;text-decoration:none;background:var(--white)}

.peek{position:absolute;left:746px;top:1141px;width:290px;height:30px;background:var(--white);border:1px solid #ddd;box-shadow:0 0 4px rgba(0,0,0,.12);padding:7px 7px 0}
.peek div{width:100%;height:30px;background:linear-gradient(90deg,#e0a98e,#c98f73 40%,#2a2220 60%,#d8d8d8)}
</style>
</head>
<body>
<div class="page">

  <header class="site-header">
    <div class="brand">
      <span class="brand-dot"></span>
      <span class="brand-name">Brightvale<br>Learning Hub</span>
    </div>
    <nav class="main-nav">
      <a href="#" style="left:266px">Home</a>
      <a href="#" class="active" style="left:356px">Financial Aid</a>
      <a href="#" style="left:503px">Cost Savings</a>
      <a href="#" style="left:654px">Colleges</a>
      <a href="#" style="left:767px">Awards</a>
      <a href="#" style="left:872px">Blog</a>
    </nav>
    <div class="social">
      <a href="#" aria-label="Social profile one" style="left:995px;background:#3b5a98"></a>
      <a href="#" aria-label="Social profile two" style="left:1033px;background:#1ea0e8"></a>
      <a href="#" aria-label="Social profile three" style="left:1073px;background:#dc3a2f"></a>
    </div>
  </header>

  <section class="hero">
    <div class="hero-photo" role="img" aria-label="Photo of four smiling young college students standing together"></div>
    <div class="hero-caption">
      <h1>Resource for an Affordable Online College Education</h1>
      <p>Brightvale Learning Hub will help you find a more affordable college experience. Look no further to find financial aid information, cost saving tips, and comprehensive college rankings focused on affordability and value.</p>
    </div>

    <form class="search-panel">
      <div class="search-head">
        <svg class="abs" style="left:16px;top:20px" width="34" height="34" viewBox="0 0 34 34"><circle cx="13" cy="13" r="9" fill="none" stroke="#111" stroke-width="4"/><line x1="20" y1="20" x2="30" y2="30" stroke="#111" stroke-width="6" stroke-linecap="round"/></svg>
        <div class="get-info">GET<br>INFO!</div>
        <span class="head-rule"></span>
        <div class="search-title">SEARCH HERE</div>
        <div class="search-sub">REQUEST MORE INFORMATION</div>
        <svg class="abs" style="left:336px;top:10px" width="32" height="46" viewBox="0 0 32 46"><path d="M10 2h12v22h8L16 44 2 24h8z" fill="#e8e8e8" stroke="#b9b9b9" stroke-width="1.5"/></svg>
      </div>

      <div class="step-no" style="top:91px">1</div>
      <div class="select is-first" style="top:80px"><span>Choose a Degree Level</span><i></i>
        <svg width="14" height="18" viewBox="0 0 14 18"><path d="M7 0l6 7H1zM7 18l6-7H1z" fill="#111"/></svg></div>

      <div class="step-no" style="top:156px">2</div>
      <div class="select" style="top:145px"><span>Choose a Category</span><i></i>
        <svg width="14" height="18" viewBox="0 0 14 18"><path d="M7 0l6 7H1zM7 18l6-7H1z" fill="#444"/></svg></div>

      <div class="step-no" style="top:221px">3</div>
      <div class="select" style="top:210px"><span style="left:28px">Choose a Subject</span><i></i>
        <svg width="14" height="18" viewBox="0 0 14 18"><path d="M7 0l6 7H1zM7 18l6-7H1z" fill="#444"/></svg></div>

      <div class="search-btn">SEARCH NOW</div>
    </form>
  </section>

  <section class="stats">
    <div class="stat-bar" style="top:11px"><b style="width:97px"></b><span>$12,500</span></div>
    <div class="stat-label" style="top:15px">AVERAGE STUDENT DEBT IN 1996</div>
    <div class="stat-bar" style="top:62px"><b style="width:143px"></b><span>$26,600</span></div>
    <div class="stat-label" style="top:67px">AVERAGE STUDENT DEBT IN 2011</div>

    <svg class="pie" width="88" height="88" viewBox="0 0 88 88">
      <circle cx="44" cy="44" r="43" fill="#0f1a1f"/>
      <path d="M44 44 L44 1 A43 43 0 1 0 81.8 64.5 Z" fill="var(--teal)"/>
      <text x="44" y="53" text-anchor="middle" font-family="Oswald,sans-serif" font-size="26" fill="#fff">66%</text>
    </svg>

    <div class="stats-copy">
      <h2>College Costs Rising &amp; Student Debt Ballooning</h2>
      <p>Brightvale Learning Hub helps students find affordable<br>college options and provides information about financial aid<br>and college rankings.</p>
    </div>
  </section>

  <article class="feature" style="left:103px;top:583px">
    <div class="feature-icon"><svg width="40" height="50" viewBox="0 0 40 50"><text x="20" y="42" text-anchor="middle" font-family="Arimo,sans-serif" font-weight="700" font-size="48" fill="#fff">$</text></svg></div>
    <div class="feature-body"><h3>Financial Aid</h3><p>The nuts of bolts of financial aid – what's available and how to apply.</p></div>
    <a class="read-more" href="#" style="top:84px">Read more</a>
  </article>

  <article class="feature" style="left:440px;top:583px">
    <div class="feature-icon"><svg width="56" height="44" viewBox="0 0 56 44"><rect x="2" y="30" width="9" height="14" fill="#fff"/><rect x="16" y="24" width="9" height="20" fill="#fff"/><rect x="30" y="18" width="9" height="26" fill="#fff"/><rect x="44" y="10" width="9" height="34" fill="#fff"/><path d="M4 22 L20 14 L32 16 L50 2" fill="none" stroke="#fff" stroke-width="3"/></svg></div>
    <div class="feature-body"><h3>Rising College Costs: Who is Helping?</h3><p>Who's helping and what does that mean for you?</p></div>
    <a class="read-more" href="#" style="top:105px">Read more</a>
  </article>

  <article class="feature" style="left:777px;top:583px">
    <div class="feature-icon"><svg width="56" height="42" viewBox="0 0 56 42"><ellipse cx="28" cy="21" rx="22" ry="16" fill="#fff"/><rect x="14" y="32" width="7" height="9" fill="#fff"/><rect x="34" y="32" width="7" height="9" fill="#fff"/><rect x="48" y="16" width="7" height="8" fill="#fff"/><text x="26" y="27" text-anchor="middle" font-family="Arimo,sans-serif" font-weight="700" font-size="15" fill="#f26c38">$</text></svg></div>
    <div class="feature-body"><h3>Affordability Tips</h3><p>Check out our tips for how you can make college more affordable</p></div>
    <a class="read-more" href="#" style="top:84px">Read more</a>
  </article>

  <article class="feature" style="left:103px;top:798px">
    <div class="feature-icon"><svg width="44" height="42" viewBox="0 0 44 42"><path d="M22 2 L42 12 H2 Z" fill="#fff"/><rect x="4" y="14" width="36" height="3" fill="#fff"/><rect x="7" y="19" width="5" height="15" fill="#fff"/><rect x="15" y="19" width="5" height="15" fill="#fff"/><rect x="24" y="19" width="5" height="15" fill="#fff"/><rect x="32" y="19" width="5" height="15" fill="#fff"/><rect x="2" y="36" width="40" height="4" fill="#fff"/></svg></div>
    <div class="feature-body" style="width:230px"><h3>Affordable Campus Colleges</h3><p>Which colleges offer the best value?</p></div>
    <a class="read-more" href="#" style="top:62px">Read more</a>
  </article>

  <article class="feature" style="left:440px;top:798px">
    <div class="feature-icon"><svg width="50" height="64" viewBox="0 0 50 64"><circle cx="25" cy="23" r="19" fill="none" stroke="#fff" stroke-width="3" stroke-dasharray="6 3"/><circle cx="25" cy="23" r="12" fill="none" stroke="#fff" stroke-width="3"/><path d="M14 38 L6 58 L14 54 L18 62 L24 42 M36 38 L44 58 L36 54 L32 62 L26 42" fill="none" stroke="#fff" stroke-width="3"/></svg></div>
    <div class="feature-body"><h3>Awards</h3><p>Awesome professors and financial aid folks working to make your life easier.</p></div>
    <a class="read-more" href="#" style="top:84px">Read more</a>
  </article>

  <article class="feature" style="left:777px;top:798px">
    <div class="feature-icon"><svg width="50" height="42" viewBox="0 0 50 42"><path d="M2 2 H30 V22 H14 L6 30 V22 H2 Z" fill="#fff"/><path d="M20 14 H48 V34 H44 V42 L36 34 H20 Z" fill="#fff" stroke="#f26c38" stroke-width="2"/></svg></div>
    <div class="feature-body"><h3>Blog</h3><p>The latest on making college affordable.</p></div>
    <a class="read-more" href="#" style="top:84px">Read more</a>
  </article>

  <article class="feature" style="left:103px;top:991px">
    <div class="feature-icon"><svg width="54" height="52" viewBox="0 0 54 52"><path d="M27 4 L52 16 L27 28 L2 16 Z" fill="#fff"/><path d="M12 22 V34 C18 40 36 40 42 34 V22 L27 30 Z" fill="#fff"/><line x1="6" y1="18" x2="6" y2="34" stroke="#fff" stroke-width="2"/><circle cx="6" cy="36" r="3" fill="#fff"/><path d="M30 40 l10 10 l4 -4 l-10 -10 z" fill="#fff" stroke="#f26c38" stroke-width="1.5"/></svg></div>
    <div class="feature-body"><h3>Affordable Online Colleges</h3><p>Find affordable online colleges that offer great value to students.</p></div>
    <a class="read-more" href="#" style="top:83px">Read more</a>
  </article>

  <article class="feature" style="left:440px;top:991px">
    <div class="feature-icon"><svg width="60" height="40" viewBox="0 0 60 40"><rect x="10" y="2" width="40" height="28" rx="2" fill="none" stroke="#fff" stroke-width="3"/><path d="M2 32 H58 L54 38 H6 Z" fill="#fff"/></svg></div>
    <div class="feature-body"><h3>College Classes Online</h3><p>Find introductory (101) college level classes offered free by top colleges</p></div>
    <a class="read-more" href="#" style="top:83px">Read more</a>
  </article>

  <div class="peek"><div role="img" aria-label="Photo of a student, partly visible at the bottom of the page"></div></div>

</div>
</body>
</html>
```